Start up business, dog breeder. Needs logo design and website.

I am a start up business looking for a logo design and a website. Silver Creek Doodles is a breeder of goldendoodles and labradoodles for home and sport. We have a strong emphasis on hunting lines within our dogs and strive to breed healthy companions for the field and the home. These dogs are a cross between golden retrievers and poodles or Labrador retrievers and poodles (some multigenerational) and possess a strong hunt drive along with the desire to please. Some people can't tolerate shedding and dander, whether due to allergies or personal preference. That's one of the things that makes these dogs so versatile - they are all low to nonshedding and allergy friendly for most people. Combine that with the intelligence, loyalty, need to please, temperament and athletic ability, and you have an amazing pet. We are marketing to people that want a nonshedding pet, and also to people who want a hunting companion. It is important to reach both groups of buyers, but not to lean too much toward either one. (The dogs flush and retrieve for bird hunters - pheasant, dove, quail, duck, etc.) They are raised, bred and trained on our small farm in Alder Ridge County, Millbrook Prairie, where they have lots of room to run, exercise and train in the prairie lands. The term "adopt" a puppy is preferred over "buy" a puppy.

I have purchased the web address with a wordpress platform through net harbor.com. I started the website using one of their templates but wasn't pleased with it - need something far more professional than I'm capable of putting together. I will need help publishing the site and brief instructions on how to change and update when I have litters for adoption. I have quite a bit of content (text) and photos put together to give an idea of what we'd like it to say....feel free to edit away! I am no writer by any means, but it will share the business concept at least.

My "style" isn't really defined for a web design, but I can tell you what I like based on how I decorate my home: I love rustic mixed with dressy/contemporary, to offset all the rough edges, if that's any help. Think pallet wood walls with a crystal chandelier. I use lots of wood, plants, and repurpose old stuff for new uses. Natural, organic, texture.

I have a facebook page, but haven't done much with it yet. www.friendnook.com/silvercreekdoodles

I have a professional photographer coming to take photos of all my breeding stock next month, but I attached some snapshot photos to use as placeholders for the time being. Also attached of photo of my husband and I as owners and operators of Silver Creek Doodles. Paul Henry Whitmore, and Rachel Whitmore

Target Market(s)

Allergy sufferers who need a low to non shedding dog
People looking to add a beautiful intelligent trainable house pet to their family
Bird and duck hunters who need a hunting companion

Industry/Entity Type

Marketing

Requirements
Must have
• 1. Adoption questionnaire for prospective buyers. Form details/fields attached. When the buyer clicks "submit" the form results should go to my email address
2. Pay pal option for deposits and final payments (we do not accept credit cards)
3. An "outdoorsy" feel. Natural. Organic.
4. We are marketing to people that want a nonshedding pet, and also to people who want a hunting companion. It is important to reach both groups of buyers, but not to lean too much toward either one.
Nice to have
• A rustic feel. Look at tamarelkfieldpups.com
Some reference to our namesake/location. "Golden Valley" is the county we live in and is named so for the surrounding croplands. Think rolling fields of wheat, pheasants, wildlife, meadows, ponds, hunting.....
Should not have
• 1. Music
2. Nothing froo-froo or silly, nothing cartoonish
3. An example of what I don't like (very homemade looking, unprofessional, terrible layout, cartoony looking) http://www.ninapups.net http://www.curlcoatnation.com

```html
<!DOCTYPE html>
<html lang="en">
<head>
<meta charset="utf-8">
<title>Silver Creek Doodles</title>
<link rel="stylesheet" href="https://fonts.googleapis.com/css2?family=Oswald:wght@400;500&family=Open+Sans:wght@400;600&display=swap">
<style>
  :root {
    --wood-dark: #1c1510;
    --wood-mid: #2e2219;
    --page-bg: #2a241e;
    --sidebar-text: #e6d7bf;
    --heading-light: #cfae8a;
    --heading-dark: #4a3a2b;
    --panel: #d6b98d;
    --panel-border: #6e655c;
    --panel-text: #3c3128;
    --nav-text: #eee3d2;
    --nav-active: #c99658;
    --button-bg: #c9a574;
    --button-text: #2a1f16;
    --footer-bar: #6e655c;
    --footer-text: #eee3d2;
  }
  * { box-sizing: border-box; margin: 0; padding: 0; }
  html, body { width: 1161px; height: 1200px; overflow: hidden; }
  body {
    position: relative;
    background: linear-gradient(90deg, var(--wood-dark) 0%, var(--wood-mid) 18%, var(--wood-dark) 40%, var(--wood-mid) 62%, var(--wood-dark) 82%, var(--wood-mid) 100%);
    font-family: "Open Sans", Arial, sans-serif;
  }
  .main-nav {
    position: absolute; top: 0; right: 144px; height: 24px;
    display: flex; align-items: center;
  }
  .main-nav a {
    color: var(--nav-text); text-decoration: none; font-size: 12.5px;
    padding: 0 10px; border-left: 1px solid #5a4d40; line-height: 22px;
  }
  .main-nav a:first-child { border-left: none; }
  .main-nav a.is-active { color: var(--nav-active); }

  .site-header {
    position: absolute; left: 125px; top: 26px; width: 912px; height: 187px;
    background: linear-gradient(100deg, #8a4f22 0%, #b5742f 22%, #d9b25c 45%, #e7c86e 60%, #9dc1cf 78%, #c98d3a 100%);
    border-top: 6px solid #a06a36; border-bottom: 5px solid #a06a36;
  }
  .brand-name {
    position: absolute; left: 34px; top: 56px; width: 440px;
    font-family: "Oswald", sans-serif; font-weight: 500; font-size: 44px;
    line-height: 1; color: #3b2a1c; text-transform: uppercase; letter-spacing: 1px;
  }

  .content-frame {
    position: absolute; left: 125px; top: 216px; width: 912px; height: 957px;
    background: var(--page-bg); border: 1px solid #4a3f35;
  }
  .sidebar {
    position: absolute; left: 30px; top: 30px; width: 154px; color: var(--sidebar-text);
    font-size: 11.8px; line-height: 13.3px; letter-spacing: -0.1px;
  }
  .sidebar h2 {
    font-family: "Oswald", sans-serif; font-weight: 400; font-size: 25px;
    color: var(--heading-light); margin: 0 0 8px 5px; line-height: 34px;
  }
  .sidebar p, .sidebar ul { margin-bottom: 24px; }
  .sidebar ul { list-style: none; }
  .sidebar .pups-text { margin-bottom: 4px; }
  .sidebar-divider {
    position: absolute; left: 195px; top: 10px; width: 2px; height: 860px; background: #8a7d70;
  }
  .btn-more {
    display: inline-block; background: var(--button-bg); color: var(--button-text);
    font-family: "Open Sans", sans-serif; font-weight: 600; font-size: 13px;
    padding: 0 5px; line-height: 18px; border: 1px solid #5a4532; text-decoration: none;
  }

  .main-panel {
    position: absolute; left: 206px; top: 20px; width: 688px; height: 841px;
    background: var(--panel); border: 4px solid var(--panel-border);
  }
  .main-panel h2 {
    position: absolute; font-family: "Oswald", sans-serif; font-weight: 500;
    font-size: 25px; color: var(--heading-dark); line-height: 34px;
  }
  .photo { position: absolute; }
  .photo-home { left: 21px; top: 47px; width: 302px; height: 397px; background: linear-gradient(180deg, #b88f6f 0%, #8d6a52 55%, #5c4a40 100%); }
  .photo-hunt { left: 356px; top: 47px; width: 303px; height: 408px; background: linear-gradient(180deg, #c9c5bd 0%, #6f5443 45%, #3e2e24 100%); }
  .caption { position: absolute; font-size: 9px; color: var(--panel-text); }
  .about-text {
    position: absolute; left: 8px; top: 528px; width: 660px;
    font-family: Arial, Helvetica, sans-serif; font-weight: 700; font-size: 10.8px;
    line-height: 25.6px; color: var(--panel-text);
  }
  .main-panel .btn-more { position: absolute; left: 8px; top: 804px; }

  .site-footer {
    position: absolute; left: 9px; top: 888px; width: 894px; height: 58px; background: var(--footer-bar);
  }
  .social-links { position: absolute; left: 10px; top: 12px; display: flex; gap: 9px; }
  .social-links span { width: 32px; height: 32px; display: block; border-radius: 2px; }
  .social-rss { background: #e07b2e; }
  .social-a { background: #6fb6dc; }
  .social-b { background: #3c5a96; }
  .social-c { background: #2f6f9e; }
  .copyright {
    position: absolute; right: 11px; top: 10px; color: var(--footer-text); font-size: 12px;
  }
</style>
</head>
<body>
  <nav class="main-nav">
    <a href="#" class="is-active">Home</a>
    <a href="#">Photos</a>
    <a href="#">Adoption</a>
    <a href="#">Contact</a>
    <a href="#">About</a>
    <a href="#">Puppies</a>
  </nav>

  <header class="site-header" role="img" aria-label="Banner of golden wheat field framed by weathered wood">
    <div class="brand-name">Silver Creek Doodles</div>
  </header>

  <div class="content-frame">
    <aside class="sidebar">
      <h2>Labradoodles</h2>
      <p>A Labradoodle is a crossbred dog created by crossing the Labrador Retriever and the Standard, Miniature or Toy Poodle. The term first appeared in 1955, but was not popularized until 1988, when the mix began to be used as allergen-free guide dog.</p>
      <h2>Our Dogs</h2>
      <ul>
        <li>Miss Clare</li>
        <li>Gypsy Girl</li>
        <li>Toby</li>
        <li>Winchester</li>
      </ul>
      <h2>New Pups</h2>
      <p class="pups-text">Gypsy and Chester will breed late winter 2014. Gypsy throws solids and parti pups - we are expecting some fantastic colors and wavy coats. She always has 6 to 8 healthy, beautiful pups. We will only be accepting 5 deposits on this litter. Please click on Adoption Link to read more about our policies, pricing and contract.</p>
      <a href="#" class="btn-more">More Info</a>
    </aside>
    <div class="sidebar-divider"></div>

    <main class="main-panel">
      <h2 style="left:8px;top:5px">Home Companions</h2>
      <h2 style="left:343px;top:5px">Hunting Companions</h2>
      <div class="photo photo-home" role="img" aria-label="Photo of a brown standard poodle sitting indoors"></div>
      <div class="caption" style="left:235px;top:448px">Image by xxxxxxxx</div>
      <div class="photo photo-hunt" role="img" aria-label="Photo of a brown doodle puppy holding a game bird"></div>
      <div class="caption" style="left:572px;top:460px">Image by xxxxxxxx</div>
      <h2 style="left:8px;top:479px">Who We Are</h2>
      <p class="about-text">Silver Creek Doodles is a breeder of goldendoodles and labradoodles for home and sport. We have a strong emphasis on hunting lines within our dogs and strive to breed healthy companions for the field and the home. These dogs are a cross between golden retrievers and poodles or Labrador retrievers and poodles (some multigenerational) and possess a strong hunt drive along with the desire to please. Some people can't tolerate shedding and dander, whether due to allergies or personal preference. That's one of the things that makes these dogs so versatile – they are all low to nonshedding and allergy friendly for most people. Combine that with the intelligence, loyalty, need to please, temperament and athletic ability, and you have an amazing pet. We are marketing to people that want a nonshedding pet, and also to people who want a hunting companion. It is important to reach both groups of buyers, but not to lean too much toward either one. Temperament and intelligence also makes them candidates for working dogs, ie therapy dog. (The dogs flush and retrieve for bird hunters – pheasant, dove, quail, duck, etc.) They are raised, bred and trained on our small farm in Alder Ridge County, Millbrook Prairie, where they have lots of room to run, exercise and train in the prairie lands.</p>
      <a href="#" class="btn-more">More Info</a>
    </main>

    <footer class="site-footer">
      <div class="social-links">
        <span class="social-rss" role="img" aria-label="News feed link"></span>
        <span class="social-a" role="img" aria-label="Social profile link"></span>
        <span class="social-b" role="img" aria-label="Social profile link"></span>
        <span class="social-c" role="img" aria-label="Social profile link"></span>
      </div>
      <div class="copyright">Copyright © 2013 Silver Creek Doodles</div>
    </footer>
  </div>
</body>
</html>
```